Re-launching marine insurance adjusting company - looking for energy

I am a sole practitioner specializing in the profession of average adjusting. There is an on-line brochure at www.rkbtnova.com I am one of only a handful of specialists in this field and I enjoy a fair amount of name recognition, domestically in the US and internationally. My principal markets are the US, the London and Scandinavian insurance markets and shipowners and insurers in Latin America.
The business is a mixture of law, accounting and insurance and my clientele relies on a time-sensitive and accurate work-product, clearly stating an insurance company's liability for a given claim. The identity needs to project gravitas rather than flash.
Since 1998 I have traded as "The Halloway Company" but have also attempted to establish the name RKBNOVA.com so that people would visit my website.
I want to implement a single identity across my stationery, business cards and website. I have come to see "The Halloway Company" as rather fatuous, since there is no company, it is just me. The Internet domain RKBNOVA is long-established and I would be reluctant to change it. I have considered trading as simply Marcus T Halloway, MTH, RKBNOVA or attempting to come up with a name that could be abbreviated to MTH, e.g. M Halloway Trelantics - but I can't find a suitable word for the second S.
Logo-wise, I have considered a stylized MTH or RKBNOVA redolent of waves of the sea. A nautical theme embodying a cargo ship, navigational beacon or lighthouse might be appropriate but these tend to be hackneyed.
I have attached a card that I mocked up at Pix, connoting stacking up numbers, which I really like, but I think it is too cryptic for people in most insurance companies, who don't particularly think laterally or they wouldn't work in marine insurance, and the card that I use currently, which I intended to be understated, but in fact it states nothing.
I have also attached my current letterhead, to demonstrate how I really need help.
Finally, I have attached a credentials sheet, to attempt to establish how narrow and deep is the professional niche that I occupy.
What I am looking to implement is a single logo, font, them and color scheme to use across my website, letterhead and business cards.
Over to the Sketch Guild...
Target Market(s)
Ship owners and insurance companies
Industry/Entity Type
Accounting

```html
<!DOCTYPE html>
<html lang="en">
<head>
<meta charset="utf-8">
<title>RKBNOVA.com Letterhead</title>
<link href="https://fonts.googleapis.com/css2?family=Old+Standard+TT:wght@400;700&display=swap" rel="stylesheet">
<style>
  :root {
    --backdrop: #ececec;
    --paper: #ffffff;
    --ink: #1a1a1a;
    --rule: #b8b8b8;
    --shadow: rgba(0,0,0,0.08);
  }
  html, body {
    margin: 0;
    padding: 0;
    width: 1200px;
    height: 1192px;
    overflow: hidden;
    background: var(--backdrop);
    font-family: "Old Standard TT", "Times New Roman", serif;
    color: var(--ink);
  }
  .letterhead {
    position: absolute;
    left: 190px;
    top: 46px;
    width: 820px;
    height: 1100px;
    background: var(--paper);
    box-shadow: 0 4px 18px var(--shadow);
  }
  .double-rule {
    position: absolute;
    left: 70px;
    right: 70px;
    height: 4px;
    border-top: 1px solid var(--rule);
    border-bottom: 1px solid var(--rule);
  }
  .rule-top { top: 70px; }
  .rule-header-bottom { top: 196px; }
  .rule-footer { top: 980px; }
  .rule-footer-bottom { top: 1058px; }
  .brand {
    position: absolute;
    top: 96px;
    left: 0;
    right: 0;
    text-align: center;
  }
  .brand-name {
    display: inline-flex;
    align-items: center;
    gap: 10px;
    font-size: 44px;
    font-weight: 400;
    line-height: 1;
    letter-spacing: -0.5px;
  }
  .brand-mark {
    width: 16px;
    height: 16px;
    border-radius: 50%;
    background: var(--ink);
  }
  .brand-tagline {
    margin-top: 6px;
    font-size: 17px;
    letter-spacing: 6px;
  }
  .contact {
    position: absolute;
    top: 996px;
    left: 0;
    right: 0;
    text-align: center;
    font-size: 13.5px;
    line-height: 1.6;
  }
  .contact b { font-weight: 700; }
</style>
</head>
<body>
  <main class="letterhead">
    <div class="double-rule rule-top"></div>
    <header class="brand">
      <div class="brand-name"><span class="brand-mark"></span>RKBNOVA.com</div>
      <div class="brand-tagline">The Halloway Company</div>
    </header>
    <div class="double-rule rule-header-bottom"></div>

    <div class="double-rule rule-footer"></div>
    <footer class="contact">
      <div><b>A:</b> 48 Harbor View Place New York, NY10099, USA</div>
      <div><b>P:</b> (555) 304 1180 | <b>F:</b> (555) 202 4471 | <b>E:</b> info@rkbnova.com / <b>W:</b> www.rkbnova.com</div>
    </footer>
    <div class="double-rule rule-footer-bottom"></div>
  </main>
</body>
</html>
```